Tech Company Letterhead/Business Cards/Envelopes

We would like a new stationary design for a technology company that develops full turnkey solutions for governments related to Data, Identity Tracking, Fingerprinting, Passport Control, and Border Protection Systems.

We would like the stationary designs to include:

Letter Head
Business Cards
Envelopes

Target Market(s)

Corporate

Industry/Entity Type

Business

Contact Information for Business Card

Details to be shared with the winner.

Font styles to use
Serif
Sans Serif

Colors
e4daeb
85abd2
3176b5
0355a3
0692cd

```html
<!DOCTYPE html>
<html lang="en">
<head>
<meta charset="utf-8">
<title>NORVEX Stationery</title>
<link rel="stylesheet" href="https://fonts.googleapis.com/css2?family=Arimo:wght@400&family=Open+Sans:wght@400;600&display=swap">
<style>
:root{
  --canvas:#e7e7e9;
  --paper:#ffffff;
  --ink:#1c1c1c;
  --brand:#2a6fb0;
  --band:#3a7ab8;
  --band-edge:#245c9e;
  --deep:#245c9e;
  --card-a:#1f5a9a;
  --card-b:#2d7ec0;
  --accent:#3a86c8;
}
*{box-sizing:border-box;margin:0;padding:0}
html,body{width:1200px;height:1000px;overflow:hidden}
body{background:var(--canvas);position:relative;font-family:"Open Sans",Arial,sans-serif;color:var(--ink)}
.sheet{position:absolute;background:var(--paper)}
.wordmark{font-family:"Open Sans",Arial,sans-serif;font-weight:600;color:var(--brand);letter-spacing:.06em;line-height:1;white-space:nowrap}
.footer-band{position:absolute;left:0;right:0;background:var(--band);border-top:3px solid var(--band-edge);display:flex;align-items:center;color:#fff;font-size:7.5px}
.footer-band .col{flex:1;text-align:center;line-height:1.45}
.footer-band .sep{width:1px;height:20px;background:rgba(255,255,255,.55)}
.footer-band svg{width:7px;height:7px;vertical-align:-1px;margin-right:2px}

/* Letterhead */
.letterhead{left:60px;top:36px;width:487px;height:689px}
.letterhead .wordmark{position:absolute;top:34px;left:0;right:0;text-align:center;font-size:34px}
.letter{position:absolute;left:43px;top:120px;width:392px;font-family:Arimo,Arial,sans-serif;font-size:8.6px;line-height:12.7px}
.letter .date{margin-bottom:13px}
.letter .recipient{margin-bottom:24px}
.letter .greeting{margin-bottom:14px}
.letter p.body{text-align:justify;margin-bottom:13px}
.signature{display:block;width:78px;height:30px;margin:4px 0 2px -6px;background:linear-gradient(90deg,#d8d8d8,#ececec);border-radius:3px}
.signer{color:var(--accent);font-size:8px;margin-left:8px}
.letterhead .footer-band{top:642px;height:35px}

/* Compliment slip */
.slip{left:586px;top:76px;width:532px;height:242px}
.slip .wordmark{position:absolute;left:20px;top:24px;font-size:23px}
.slip .label{position:absolute;right:29px;top:28px;font-size:10px;letter-spacing:.02em}
.slip .footer-band{top:207px;height:35px;padding:0 20px 0 40px}

/* Envelope */
.envelope{left:586px;top:370px;width:532px;height:242px}
.envelope svg.flap{position:absolute;left:0;top:0}
.envelope .wordmark{position:absolute;left:0;right:0;top:24px;text-align:center;color:#fff;font-size:24px}

/* Cards */
.card{position:absolute;width:344px;height:203px;border-radius:10px;overflow:hidden}
.card-front{left:270px;top:753px;background:linear-gradient(135deg,var(--card-a),var(--card-b))}
.card-front .wordmark{position:absolute;left:0;right:0;top:78px;text-align:center;color:#fff;font-size:50px;letter-spacing:.1em}
.card-front .url{position:absolute;left:0;right:0;top:180px;text-align:center;color:#fff;font-size:8.5px}
.card-back{left:665px;top:754px;background:var(--paper)}
.card-back .tab{position:absolute;left:0;top:23px;width:20px;height:27px;background:var(--deep)}
.card-back .name{position:absolute;left:27px;top:25px;font-size:12px;color:var(--accent);line-height:1}
.card-back .role{position:absolute;left:27px;top:40px;font-size:7px;font-weight:600;letter-spacing:.02em}
.card-back .wordmark{position:absolute;right:20px;top:70px;font-size:28px}
.card-back .contact{position:absolute;left:27px;top:127px;font-size:8.5px;line-height:12px;color:#555}
.card-back .contact b{color:var(--accent);font-weight:400}
.card-back .footer-band{top:159px;height:33px;justify-content:space-between;padding:0 16px 0 26px;font-size:8.5px}
.card-back .footer-band .col{flex:none;text-align:left;line-height:1.3}
</style>
</head>
<body>

<section class="sheet letterhead">
  <div class="wordmark">NORVEX</div>
  <div class="letter">
    <div class="date">29 August, 2016</div>
    <div class="recipient">Mr. Mark Ellis<br>President<br>NORVEX Corporation<br>111 Street Name, Suite#<br>City State, 12345</div>
    <div class="greeting">Dear Mr. Mark,</div>
    <p class="body">Lorem ipsum dolor sit amet, cu augue evertitur definitiones per, eum impetus tamquam dissentiet in. Enim sensibus ullamcorper mel ei, sit accumsan dissentias ad, usu cu fugit melius prodesset. Ea mei ancillae mandamus salutatus. Has ad sumo prima, eam in illum dissentiet, no sale graeci pro. Noster iuvaret moderatius no per.</p>
    <p class="body">Movet soluta semper has te, graece cetero intellegat usu id. Everti meliore et vel, cu mea idque utroque nostrum. Cu ius lorem constituam, alii debet percipit vix at. Modus altera sea ei, vix dico constituto te. Cu eam nibh putent, est soluta reformidans eu. Esse nominavi vim ad, ne populo evertitur conceptam per.</p>
    <p class="body">Usu zril facilisis laboramus eu, pro harum ancillae scripserit ad, pro in zril vocibus graecis. Duo id elit vocent, id nobis aperiam luptatum per. Est illum mediocrem reprehendunt ea, ius ut novum mazim deleniti. Et eos possit temporibus, erroribus referrentur et est. Usu purto virtute consetetur ea, ne pri novum mazim prompta.</p>
    <p class="body">Nisl natum dicta usu no, sea id vidit forensibus, nec an prompta periculis. Eam id veniam accusata. Nulla adolescens constituam an his. Dolore constituam ex sea. Te pri commodo feugait laboramus, qui petentium consectetuer ea, an duo falli ridens graeco. Mei verear nostrud discere ei, postea noluisse honestatis eam eu.</p>
    <div>Sincerely Yours,</div>
    <span class="signature" role="img" aria-label="Handwritten signature of Mark Ellis"></span>
    <div class="signer">MARK ELLIS</div>
  </div>
  <div class="footer-band">
    <div class="col">4120 Larkspur Ave. Westbrook, IL 60411</div>
    <div class="sep"></div>
    <div class="col">
      <svg viewBox="0 0 10 10"><circle cx="5" cy="5" r="4.2" fill="none" stroke="#fff" stroke-width="1"/><path d="M3.5 3h1l.5 1.3-.7.5a3 3 0 0 0 1 1l.5-.7L7 5.6v1A.7.7 0 0 1 6.3 7 4 4 0 0 1 3 3.7.7.7 0 0 1 3.5 3z" fill="#fff"/></svg>(555) 207-3188<br>
      <svg viewBox="0 0 10 10"><rect x="1" y="2.5" width="8" height="5.5" fill="none" stroke="#fff" stroke-width="1"/><path d="M1 2.5l4 3 4-3" fill="none" stroke="#fff" stroke-width="1"/></svg>mail@norvex.com
    </div>
    <div class="sep"></div>
    <div class="col">www.norvextech.com</div>
  </div>
</section>

<section class="sheet slip">
  <div class="wordmark">NORVEX</div>
  <div class="label">WITH COMPLIMENTS</div>
  <div class="footer-band">
    <div class="col">4120 Larkspur Ave. Westbrook, IL 60411</div>
    <div class="sep"></div>
    <div class="col">
      <svg viewBox="0 0 10 10"><circle cx="5" cy="5" r="4.2" fill="none" stroke="#fff" stroke-width="1"/><path d="M3.5 3h1l.5 1.3-.7.5a3 3 0 0 0 1 1l.5-.7L7 5.6v1A.7.7 0 0 1 6.3 7 4 4 0 0 1 3 3.7.7.7 0 0 1 3.5 3z" fill="#fff"/></svg>(555) 207-3188<br>
      <svg viewBox="0 0 10 10"><rect x="1" y="2.5" width="8" height="5.5" fill="none" stroke="#fff" stroke-width="1"/><path d="M1 2.5l4 3 4-3" fill="none" stroke="#fff" stroke-width="1"/></svg>mail@norvex.com
    </div>
    <div class="sep"></div>
    <div class="col">www.norvextech.com</div>
  </div>
</section>

<section class="sheet envelope">
  <svg class="flap" width="532" height="76" viewBox="0 0 532 76">
    <path d="M0 0H532V10L520 63Q517 72 507 72H25Q15 72 12 63L0 10Z" fill="var(--deep)"/>
  </svg>
  <div class="wordmark">NORVEX</div>
</section>

<section class="card card-front">
  <div class="wordmark">NORVEX</div>
  <div class="url">www.norvextech.com</div>
</section>

<section class="card card-back">
  <div class="tab"></div>
  <div class="name">Mark T. Ellis</div>
  <div class="role">DIRECTOR</div>
  <div class="wordmark">NORVEX</div>
  <div class="contact"><b>P:</b> (555) 207-3188<br><b>T:</b> mail@norvex.com</div>
  <div class="footer-band">
    <div class="col">4120 Larkspur Ave.<br>Westbrook, IL 60411</div>
    <div class="col">www.norvextech.com</div>
  </div>
</section>

</body>
</html>
```